Voltaxe

We need graphic design similar to the ones attached.
Also can be found at: http://www.morvanta.example/technology/steady-link-merging/

We are starting new company that uses the bonding of network to remote locations.

Target Market(s)

Engineers, IT, procurement

Industry/Entity Type

Graphic Design

Font styles to use
Sans Serif

```html
<!DOCTYPE html>
<html lang="en">
<head>
<meta charset="utf-8">
<title>Voltaxe – Bonded Network Overview</title>
<link href="https://fonts.googleapis.com/css2?family=Arimo:wght@400;700&display=swap" rel="stylesheet">
<style>
  :root {
    --bg: #ffffff;
    --ink: #111111;
    --lte-cyan: #00c3f2;
    --lte-red: #ef4b68;
    --lte-lime: #c6c92d;
    --lte-purple: #a45fa8;
    --trunk-blue: #5f9ad8;
    --arc-blue: #8fb7e6;
    --badge-yellow: #fde5a2;
    --globe-deep: #0e3f93;
    --globe-mid: #2a7fd4;
    --globe-light: #7fc1f2;
    --rim: #d9d9d9;
    --landline: #0b0b0b;
  }
  html, body {
    margin: 0;
    padding: 0;
    width: 1200px;
    height: 1000px;
    overflow: hidden;
    background: var(--bg);
  }
  .canvas {
    position: relative;
    width: 1200px;
    height: 1000px;
    font-family: "Arimo", Arial, sans-serif;
    color: var(--ink);
  }
  .diagram { position: absolute; inset: 0; }
  .label { font-family: "Arimo", Arial, sans-serif; fill: var(--ink); }
  .label-title { font-size: 15px; }
  .label-small { font-size: 13px; }
  .label-internet { font-size: 19px; }
  .lte-tag { font-size: 8px; font-weight: 700; fill: var(--ink); }
  .step-number { font-size: 24px; font-weight: 700; fill: #ffffff; }
  .landline-text { font-size: 15px; fill: #ffffff; }
</style>
</head>
<body>
<div class="canvas">
<svg class="diagram" width="1200" height="1000" viewBox="0 0 1200 1000" xmlns="http://www.w3.org/2000/svg">
  <defs>
    <radialGradient id="globe-fill" cx="45%" cy="35%" r="70%">
      <stop offset="0" stop-color="var(--globe-light)"/>
      <stop offset="0.55" stop-color="var(--globe-mid)"/>
      <stop offset="1" stop-color="var(--globe-deep)"/>
    </radialGradient>
    <linearGradient id="arc-fade-top" x1="0" y1="0" x2="1" y2="0">
      <stop offset="0" stop-color="var(--arc-blue)" stop-opacity="0"/>
      <stop offset="0.5" stop-color="var(--arc-blue)" stop-opacity="0.45"/>
      <stop offset="1" stop-color="var(--arc-blue)" stop-opacity="0"/>
    </linearGradient>
    <linearGradient id="arc-fade-bottom" x1="0" y1="0" x2="1" y2="0">
      <stop offset="0" stop-color="var(--arc-blue)" stop-opacity="0.1"/>
      <stop offset="0.5" stop-color="var(--arc-blue)" stop-opacity="0.9"/>
      <stop offset="1" stop-color="var(--arc-blue)" stop-opacity="0.1"/>
    </linearGradient>
    <linearGradient id="side-arc" x1="0" y1="0" x2="0" y2="1">
      <stop offset="0" stop-color="var(--arc-blue)" stop-opacity="0.1"/>
      <stop offset="0.5" stop-color="var(--arc-blue)" stop-opacity="0.9"/>
      <stop offset="1" stop-color="var(--arc-blue)" stop-opacity="0.1"/>
    </linearGradient>
    <linearGradient id="site-photo" x1="0" y1="0" x2="0" y2="1">
      <stop offset="0" stop-color="#c9d4dc"/>
      <stop offset="0.5" stop-color="#9a8a66"/>
      <stop offset="1" stop-color="#7d6f52"/>
    </linearGradient>
    <linearGradient id="office-photo" x1="0" y1="0" x2="0" y2="1">
      <stop offset="0" stop-color="#eef2f5"/>
      <stop offset="0.6" stop-color="#8c9399"/>
      <stop offset="1" stop-color="#b8bcbf"/>
    </linearGradient>
    <radialGradient id="lock-fill" cx="50%" cy="40%" r="60%">
      <stop offset="0" stop-color="#2f86e0"/>
      <stop offset="1" stop-color="#0a2c6b"/>
    </radialGradient>
  </defs>

  <!-- Header label -->
  <text class="label label-small" x="588" y="237" text-anchor="middle">Bonded Unbreakable VPN</text>

  <!-- Top halo arc -->
  <path d="M428 340 A170 170 0 0 1 752 340 L730 350 A150 150 0 0 0 450 350 Z" fill="url(#arc-fade-top)"/>

  <!-- Bottom Internet arc -->
  <path d="M438 640 Q590 760 748 640 L745 660 Q590 745 440 660 Z" fill="url(#arc-fade-bottom)"/>
  <path d="M445 650 Q590 735 742 650" fill="none" stroke="var(--arc-blue)" stroke-width="14" stroke-opacity="0.4"/>
  <text class="label label-internet" x="586" y="699" text-anchor="middle">Internet</text>

  <!-- Globe -->
  <circle cx="590" cy="515" r="165" fill="none" stroke="var(--globe-light)" stroke-width="2" stroke-opacity="0.7"/>
  <circle class="globe" cx="590" cy="515" r="152" fill="url(#globe-fill)" role="img" aria-label="Illustrated globe with world map and glowing network connection points"/>

  <!-- Trunk ribbon to home office -->
  <path d="M540 338 C640 315 720 330 760 360 C810 400 840 440 872 456 L872 568 C845 520 810 450 770 410 C720 370 650 350 560 350 Z" fill="var(--trunk-blue)" opacity="0.95"/>

  <!-- LTE ribbons -->
  <path d="M322 455 C400 420 470 350 600 330 L600 338 C480 360 410 440 322 477 Z" fill="var(--lte-cyan)"/>
  <path d="M322 484 C410 440 475 365 600 338 L600 346 C490 372 420 465 322 506 Z" fill="var(--lte-red)"/>
  <path d="M322 512 C415 460 480 380 600 346 L600 354 C495 384 428 488 322 534 Z" fill="var(--lte-lime)"/>
  <path d="M322 540 C420 480 485 395 600 354 L600 362 C500 398 435 510 322 564 Z" fill="var(--lte-purple)"/>

  <!-- LTE tags -->
  <g class="lte-tags">
    <rect x="293" y="455" width="29" height="22" fill="var(--lte-cyan)"/>
    <text class="lte-tag" x="307.5" y="464" text-anchor="middle">4G</text>
    <text class="lte-tag" x="307.5" y="473" text-anchor="middle">LTE</text>
    <rect x="293" y="484" width="29" height="22" fill="var(--lte-red)"/>
    <text class="lte-tag" x="307.5" y="493" text-anchor="middle">4G</text>
    <text class="lte-tag" x="307.5" y="502" text-anchor="middle">LTE</text>
    <rect x="293" y="512" width="29" height="22" fill="var(--lte-lime)"/>
    <text class="lte-tag" x="307.5" y="521" text-anchor="middle">4G</text>
    <text class="lte-tag" x="307.5" y="530" text-anchor="middle">LTE</text>
    <rect x="293" y="540" width="29" height="24" fill="var(--lte-purple)"/>
    <text class="lte-tag" x="307.5" y="550" text-anchor="middle">4G</text>
    <text class="lte-tag" x="307.5" y="560" text-anchor="middle">LTE</text>
  </g>

  <!-- Land line block -->
  <rect x="874" y="456" width="29" height="112" fill="var(--landline)"/>
  <text class="landline-text" transform="translate(894 512) rotate(-90)" text-anchor="middle">Land Line</text>

  <!-- Lock badge -->
  <circle cx="580" cy="284" r="33" fill="#6d6f73"/>
  <circle cx="580" cy="284" r="30" fill="url(#lock-fill)"/>
  <path d="M571 282 V274 A9 9 0 0 1 589 274 V282" fill="none" stroke="#ffffff" stroke-width="4"/>
  <rect x="567" y="281" width="26" height="21" rx="3" fill="#ffffff"/>
  <circle cx="580" cy="290" r="3" fill="#2f86e0"/>
  <rect x="579" y="290" width="2" height="6" fill="#2f86e0"/>

  <!-- Remote office -->
  <text class="label label-title" x="94" y="385">Offsite Operations /</text>
  <text class="label label-title" x="94" y="405">Remote Office</text>
  <path d="M200 405 A95 95 0 0 1 268 540 L258 532 A82 82 0 0 0 198 418 Z" fill="url(#side-arc)"/>
  <circle cx="177" cy="497" r="84" fill="var(--rim)"/>
  <circle class="site-photo" cx="177" cy="497" r="79" fill="url(#site-photo)" role="img" aria-label="Photo of a remote drilling rig site on open plains"/>

  <!-- Step 2 -->
  <text class="label label-small" x="287" y="376">Add <tspan font-weight="700">VSAT</tspan> to furter</text>
  <text class="label label-small" x="287" y="393">strengthen</text>
  <text class="label label-small" x="287" y="411">your connection</text>
  <circle cx="307" cy="432" r="17" fill="var(--badge-yellow)"/>
  <text class="step-number" x="307" y="441" text-anchor="middle">2</text>

  <!-- Home office -->
  <text class="label label-title" x="992" y="429">Home office</text>
  <path d="M970 428 A95 95 0 0 0 918 560 L930 552 A82 82 0 0 1 975 441 Z" fill="url(#side-arc)"/>
  <circle cx="1016" cy="517" r="84" fill="var(--rim)"/>
  <circle class="office-photo" cx="1016" cy="517" r="79" fill="url(#office-photo)" role="img" aria-label="Photo of a modern glass headquarters office building"/>

  <!-- Step 1 -->
  <circle cx="131" cy="633" r="17" fill="var(--badge-yellow)"/>
  <text class="step-number" x="131" y="642" text-anchor="middle">1</text>
  <text class="label label-small" x="160" y="630">Combine the bandwidth of up to</text>
  <text class="label label-small" x="160" y="647">4 providers for blazing fast access</text>
  <text class="label label-small" x="160" y="664">to head office</text>

  <!-- Step 3 -->
  <circle cx="887" cy="638" r="17" fill="var(--badge-yellow)"/>
  <text class="step-number" x="887" y="647" text-anchor="middle">3</text>
  <text class="label label-small" x="918" y="632">Remote offices are able to access</text>
  <text class="label label-small" x="918" y="649">HQ resources as if they were on the</text>
  <text class="label label-small" x="918" y="666">same local network</text>
</svg>
</div>
</body>
</html>
```